Forex Trading Company needs 4 slides for website

We need 4 sliders for website for a forex and cfd trading company based in Singapore, UK and USA called "Pelmo". We have developed and provide leading online forex and cfd trading. Access to our trading tools are free, on our most popular platform. With strategy centers, pattern recognition software, sophisticated charting packages and actionable market insight we give you the tools you need to succeed. We would like to see designs that use #FFFFFF, #282828, #F05123, #CE2327 colors. The final design should communicate financial safety and growth. You can view the website at www.pelmo.com. The sliders need to replace what is currently there. Currently there are only 3 sliders, an image of the Vardwick computer screen and 2 Quillbay 4 mobile images.
Attached is the text that will need to go into each slide.
Any questions in relation to clarification, please just ask.
Each slider needs to be 960 x 300px.

```html
<!DOCTYPE html>
<html lang="en">
<head>
<meta charset="utf-8">
<title>Pelmo – Insights Slide</title>
<link rel="stylesheet" href="https://fonts.googleapis.com/css2?family=Roboto+Condensed:wght@300;400;700&display=swap">
<style>
  :root {
    --white: #FFFFFF;
    --ink: #282828;
    --orange: #F05123;
    --red: #CE2327;
    --red-deep: #A8141A;
    --red-button: #D92A2E;
    --chart-line: rgba(255,255,255,0.16);
    --chart-body: rgba(110,0,6,0.35);
    --chart-label: rgba(255,255,255,0.35);
  }
  * { box-sizing: border-box; margin: 0; padding: 0; }
  html, body {
    width: 1200px;
    height: 375px;
    overflow: hidden;
    background: var(--white);
  }
  .slide {
    position: relative;
    width: 1200px;
    height: 375px;
    overflow: hidden;
    font-family: "Roboto Condensed", "Arial Narrow", sans-serif;
    color: var(--white);
    background: radial-gradient(ellipse at 80% 35%, #D92A2E 0%, var(--red) 45%, var(--red-deep) 100%);
  }
  .market-chart {
    position: absolute;
    left: 600px;
    top: 0;
    width: 600px;
    height: 375px;
  }
  .market-chart__label {
    font-family: "Roboto Condensed", "Arial Narrow", sans-serif;
    font-size: 11px;
    fill: var(--chart-label);
  }
  .slide__photo {
    position: absolute;
    left: 0;
    top: 0;
    width: 650px;
    height: 375px;
    background:
      linear-gradient(90deg, rgba(206,35,39,0) 90%, rgba(206,35,39,0.9) 100%),
      linear-gradient(160deg, #F4F5F5 0%, #E6E8E9 35%, #C3C7CA 62%, #6E7377 88%, #4A4E52 100%);
  }
  .slider-dots {
    position: absolute;
    top: 24px;
    left: 1052px;
    display: flex;
    gap: 14px;
  }
  .slider-dots__dot {
    width: 16px;
    height: 16px;
    border-radius: 50%;
    background: var(--white);
    box-shadow: 0 1px 3px rgba(0,0,0,0.35);
  }
  .slider-dots__dot--active {
    background: var(--orange);
    border: 4px solid var(--white);
  }
  .headline {
    position: absolute;
    left: 678px;
    top: 82px;
    font-size: 41px;
    line-height: 50px;
    font-weight: 300;
    letter-spacing: -0.3px;
    white-space: nowrap;
  }
  .headline strong { font-weight: 700; }
  .learn-more {
    position: absolute;
    left: 887px;
    top: 208px;
    display: flex;
    align-items: center;
    gap: 16px;
    font-size: 29px;
    font-weight: 700;
    color: var(--white);
    text-decoration: none;
    letter-spacing: 0.3px;
  }
  .button {
    position: absolute;
    top: 300px;
    height: 56px;
    display: flex;
    align-items: center;
    border-radius: 3px;
    color: var(--white);
    text-decoration: none;
    font-size: 18px;
    font-weight: 400;
    white-space: nowrap;
    box-shadow: 0 2px 4px rgba(0,0,0,0.25);
  }
  .button--open { left: 658px; width: 202px; background: var(--orange); }
  .button--practice { left: 871px; width: 294px; background: var(--red-button); }
  .button__icon {
    width: 52px;
    height: 38px;
    display: flex;
    align-items: center;
    justify-content: center;
    border-right: 1px solid rgba(255,255,255,0.7);
    margin-right: 11px;
  }
</style>
</head>
<body>
<main class="slide">
  <svg class="market-chart" viewBox="600 0 600 375" aria-hidden="true">
    <g stroke="var(--chart-line)" stroke-width="1">
      <line x1="600" y1="47" x2="1200" y2="47"/>
      <line x1="600" y1="126" x2="1200" y2="126"/>
      <line x1="600" y1="160" x2="1200" y2="160"/>
      <line x1="600" y1="274" x2="1200" y2="274"/>
    </g>
    <g stroke="var(--chart-line)" stroke-width="1" stroke-dasharray="1 4">
      <line x1="760" y1="200" x2="760" y2="375"/>
      <line x1="860" y1="200" x2="860" y2="375"/>
      <line x1="960" y1="200" x2="960" y2="375"/>
      <line x1="1060" y1="200" x2="1060" y2="375"/>
      <line x1="700" y1="320" x2="1200" y2="320"/>
      <line x1="700" y1="345" x2="1200" y2="345"/>
    </g>
    <g class="market-chart__candles" stroke="var(--chart-line)" fill="var(--chart-body)">
      <path d="M640 300V350M656 285V340M672 290V345M688 270V330M704 260V320M720 270V335M736 250V310M752 235V300M768 245V305M784 225V290M800 210V280M816 220V290M832 200V270M848 190V255M864 195V265M880 175V245M896 165V235M912 170V240M928 150V225M944 140V210M960 150V220M976 130V200M992 120V190M1008 125V195M1024 105V175M1040 95V165M1056 100V170M1072 80V150M1088 70V140M1104 75V150M1120 55V130M1136 45V115M1152 50V125M1168 30V105M1184 20V95"/>
      <rect x="636" y="310" width="8" height="25"/>
      <rect x="652" y="295" width="8" height="30"/>
      <rect x="668" y="300" width="8" height="20"/>
      <rect x="684" y="280" width="8" height="35"/>
      <rect x="700" y="272" width="8" height="28"/>
      <rect x="716" y="280" width="8" height="30"/>
      <rect x="732" y="258" width="8" height="32"/>
      <rect x="748" y="245" width="8" height="40"/>
      <rect x="764" y="255" width="8" height="25"/>
      <rect x="780" y="232" width="8" height="38"/>
      <rect x="796" y="220" width="8" height="35"/>
      <rect x="812" y="228" width="8" height="30"/>
      <rect x="828" y="210" width="8" height="40"/>
      <rect x="844" y="200" width="8" height="30"/>
      <rect x="860" y="205" width="8" height="35"/>
      <rect x="876" y="185" width="8" height="40"/>
      <rect x="892" y="172" width="8" height="38"/>
      <rect x="908" y="180" width="8" height="30"/>
      <rect x="924" y="160" width="8" height="40"/>
      <rect x="940" y="150" width="8" height="35"/>
      <rect x="956" y="158" width="8" height="30"/>
      <rect x="972" y="138" width="8" height="42"/>
      <rect x="988" y="130" width="8" height="35"/>
      <rect x="1004" y="135" width="8" height="30"/>
      <rect x="1020" y="115" width="8" height="38"/>
      <rect x="1036" y="102" width="8" height="40"/>
      <rect x="1052" y="110" width="8" height="30"/>
      <rect x="1068" y="90" width="8" height="38"/>
      <rect x="1084" y="78" width="8" height="40"/>
      <rect x="1100" y="85" width="8" height="35"/>
      <rect x="1116" y="65" width="8" height="40"/>
      <rect x="1132" y="52" width="8" height="38"/>
      <rect x="1148" y="60" width="8" height="35"/>
      <rect x="1164" y="40" width="8" height="40"/>
      <rect x="1180" y="30" width="8" height="38"/>
    </g>
    <text class="market-chart__label" x="1124" y="44">23.6</text>
    <text class="market-chart__label" x="1124" y="123">50.0</text>
    <text class="market-chart__label" x="1124" y="157">61.8</text>
    <text class="market-chart__label" x="1120" y="271">100.0</text>
  </svg>

  <div class="slide__photo" role="img" aria-label="Office presentation: an analyst explains charts on a whiteboard to three seated colleagues"></div>

  <div class="slider-dots" aria-label="Slide navigation">
    <span class="slider-dots__dot"></span>
    <span class="slider-dots__dot slider-dots__dot--active"></span>
    <span class="slider-dots__dot"></span>
    <span class="slider-dots__dot"></span>
  </div>

  <h1 class="headline">Insights from <strong>Fund Managers,</strong><br><strong>Economist</strong> and <strong>Analysts</strong></h1>

  <a class="learn-more" href="#">LEARN MORE
    <svg width="50" height="24" viewBox="0 0 50 24" aria-hidden="true" fill="none" stroke="#FFFFFF" stroke-width="3.5" stroke-linecap="square">
      <polyline points="4,3 13,12 4,21"/>
      <polyline points="20,3 29,12 20,21"/>
      <polyline points="36,3 45,12 36,21"/>
    </svg>
  </a>

  <a class="button button--open" href="#">
    <span class="button__icon">
      <svg width="28" height="28" viewBox="0 0 30 30" aria-hidden="true">
        <circle cx="15" cy="15" r="14" fill="#FFFFFF"/>
        <circle cx="13" cy="11" r="4" fill="#F05123"/>
        <path d="M6 22c1-4 4-6 7-6s6 2 7 6z" fill="#F05123"/>
        <path d="M21 8v6M18 11h6" stroke="#F05123" stroke-width="2"/>
      </svg>
    </span>
    OPEN ACCOUNT
  </a>

  <a class="button button--practice" href="#">
    <span class="button__icon">
      <svg width="28" height="28" viewBox="0 0 30 30" aria-hidden="true">
        <circle cx="15" cy="15" r="14" fill="#FFFFFF"/>
        <circle cx="15" cy="11" r="4" fill="#D92A2E"/>
        <path d="M8 22c1-4 4-6 7-6s6 2 7 6z" fill="#D92A2E"/>
      </svg>
    </span>
    OPEN PRACTICE ACCOUNT
  </a>
</main>
</body>
</html>
```